Stationary Design (using existing logo)

Stationary (print and electronic version for Word/email), envelope, and fax cover. All companies are part of same family or course so designs can be the same, or essentially the same. Use the logos attached, same font and colors.

Target Market(s)

Real estate professionals. Investors and other property owners. Financial professionals.

Industry/Entity Type

Real Estate

Font styles to use
Serif

Requirements
Must have
• Should be a serious, sophisticated design in colors that match the business cards we uploaded. Design needs to match the color and fonts in the attached business cards. Can use the same design for each company, just change logo and color.
Should not have
• Nothing quirky or cute.

```html
<!DOCTYPE html>
<html lang="en">
<head>
<meta charset="utf-8">
<title>Meridane Realty Group – Stationery</title>
<link rel="stylesheet" href="https://fonts.googleapis.com/css2?family=Cinzel:wght@600&family=Questrial&display=swap">
<style>
:root{
  --stage:#d4d4d4;
  --paper:#f2f2f2;
  --folder:#dcdcdd;
  --navy:#1f3b82;
  --taupe:#8b8278;
  --taupe-light:#b9b3ab;
  --ice:#bcd4e6;
  --ink:#2a2a2a;
}
*{box-sizing:border-box;margin:0;padding:0}
html,body{width:1200px;height:1000px;overflow:hidden}
body{background:var(--stage);position:relative;font-family:"Questrial",sans-serif;color:var(--ink)}
.piece{position:absolute;background:var(--paper);box-shadow:0 1px 3px rgba(0,0,0,.25);overflow:hidden}
.metal-bar{position:absolute;left:0;right:0;top:0;height:5px;background:linear-gradient(90deg,var(--taupe),var(--taupe-light) 45%,var(--ice) 55%,var(--taupe-light) 65%,var(--taupe))}
.navy-bar{position:absolute;left:0;right:0;bottom:0;height:5px;background:var(--navy)}
.wordmark{position:absolute;font-family:"Cinzel",serif;font-weight:600;color:var(--navy);text-align:center;line-height:1.15;letter-spacing:.04em}
.wordmark span{display:block}

/* folder */
.folder{left:152px;top:42px;width:430px;height:558px;background:linear-gradient(180deg,#e4e4e5,var(--folder));border-radius:4px}
.folder-spine{position:absolute;left:0;top:0;bottom:0;width:28px;border-right:1px solid #c6c6c8;background:linear-gradient(90deg,#e6e6e7,#d9d9da)}
.folder .wordmark{left:28px;right:0;top:100px;font-size:27px}
.folder .wordmark span+span{font-size:11px;letter-spacing:.2em;margin-top:4px}

/* letterhead */
.letterhead{left:616px;top:61px;width:417px;height:539px}
.letterhead .wordmark{left:38px;top:50px;font-size:20px;text-align:left}
.letterhead .wordmark span+span{font-size:8px;letter-spacing:.2em;margin-top:2px}
.contact{position:absolute;font-size:5.6px;line-height:7.4px;color:var(--ink)}
.letterhead .contact{left:304px;top:33px}
.contact .row{display:flex;align-items:center;gap:3px}
.icon{width:5px;height:5px;background:var(--navy);border-radius:1px;display:inline-block}
.contact .addr{margin-top:3px}
.letter-body{position:absolute;left:38px;top:172px;width:342px;font-size:5.6px;line-height:7.3px;text-align:justify}
.letter-body p{margin-bottom:7.3px}
.letter-body .salutation{font-weight:bold}
.signoff{position:absolute;left:38px;top:348px;font-size:5.6px;line-height:7.3px}
.signoff b{display:block}
.signature{position:absolute;left:88px;top:342px;width:84px;height:30px}

/* DL envelope front */
.env-front{left:117px;top:629px;width:466px;height:202px}
.env-front .wordmark{left:20px;top:30px;font-size:17px;text-align:left}
.env-front .wordmark span+span{font-size:6.5px;letter-spacing:.2em;margin-top:1px}
.env-front .return{position:absolute;left:49px;top:176px;font-size:5.8px;line-height:7.4px;text-align:center}

/* envelope back */
.env-back{left:616px;top:629px;width:466px;height:202px;background:#f1f1f1}
.env-back svg{position:absolute;left:0;top:0}
.env-back .wordmark{left:0;right:0;top:28px;font-size:9px;letter-spacing:.12em}
.env-back .web{position:absolute;left:0;right:0;top:178px;text-align:center;font-size:5.8px}

/* business cards */
.card{top:862px;width:173px;height:97px}
.card-front{left:410px}
.card-front .wordmark{left:14px;top:44px;font-size:11px;text-align:left}
.card-front .wordmark span+span{font-size:4.4px;letter-spacing:.18em}
.card-back{left:616px}
.card-back .wordmark{left:11px;top:46px;font-size:11px;text-align:left}
.card-back .wordmark span+span{font-size:4.4px;letter-spacing:.18em}
.card-back .divider{position:absolute;left:93px;top:30px;width:1px;height:50px;background:#cfcfcf}
.card-back .person{position:absolute;left:98px;top:26px;font-size:4.4px;line-height:5.6px}
.card-back .person .name{color:var(--navy);font-size:5.6px;font-weight:bold}
.card-back .person .title{margin-bottom:3px}
.card-back .icon{width:3.6px;height:3.6px}
</style>
</head>
<body>

<section class="piece folder" aria-label="Presentation folder">
  <div class="folder-spine"></div>
  <div class="wordmark"><span>Meridane</span><span>Realty Group LLC</span></div>
</section>

<section class="piece letterhead" aria-label="Letterhead">
  <div class="metal-bar"></div>
  <div class="wordmark"><span>Meridane</span><span>Realty Group LLC</span></div>
  <div class="contact">
    <div class="row"><i class="icon"></i>555.014.2290</div>
    <div class="row"><i class="icon"></i>info@meridanerealty.com</div>
    <div class="row"><i class="icon"></i>www.meridanerealty.com</div>
    <div class="addr">1480 W Larkfield Ave.<br>Springdale, IL 60612</div>
  </div>
  <div class="letter-body">
    <p class="salutation">Dear sir,</p>
    <p>Communication is a very integral part of living creatures, animals and humans. Communication may be verbal or written. Written communication however is only applicable to human beings. Can you even imagine a world without communication? Verbal communication can be through telephones, webcams or in person. Written communication is through letters, emails and mobile phone messages.</p>
    <p>In today's world of great inventions and technology, letters have somehow become redundant. It is the time for text messages or chats. But they still can communicate a lot more than all other modes of communication. Organizations and various government departments still bank on letters as a strong medium of communication. There is no comparison in costs of sending letters as compared to costs of mobile phone messages though – letters are far cheaper. Letters now commonly known as "hard copy documents" are considered more relevant and important than email copies of text messages as proof or evidence of some sort.</p>
    <p>Letters speak volumes about a person or an organization that writes it. So one must take utmost care ensuring that the language used in any letter is appropriate for the occasion for which it is being written. Since a letter is also a written proof or document, if there are certain things that should not form a part of it, then that too should be carefully handled.</p>
    <p>Writing a good letter is an art. But if for some reason someone is unable to write that perfect letter, these different types of letters provide a base for you to build on. Sample letters have been given for everyone to understand what all information needs to form a part of the letter type and then it can be customized.</p>
  </div>
  <div class="signoff">Yours Sincerely,<b>Elin Varro</b></div>
  <div class="signature" role="img" aria-label="Handwritten signature" style="background:linear-gradient(90deg,rgba(90,110,190,0),rgba(90,110,190,.12),rgba(90,110,190,0))"></div>
  <div class="navy-bar"></div>
</section>

<section class="piece env-front" aria-label="Envelope front">
  <div class="metal-bar"></div>
  <div class="wordmark"><span>Meridane</span><span>Realty Group LLC</span></div>
  <div class="return">1480 W Larkfield Ave.<br>Springdale, IL 60612</div>
  <div class="navy-bar"></div>
</section>

<section class="piece env-back" aria-label="Envelope back">
  <svg width="466" height="202" viewBox="0 0 466 202" aria-hidden="true">
    <path d="M0 0 H466 L444 66 Q442 72 434 72 H32 Q24 72 22 66 Z" fill="#e6e6e7" stroke="#d2d2d3" stroke-width="1"/>
  </svg>
  <div class="wordmark">Meridane</div>
  <div class="web">www.meridanerealty.com</div>
</section>

<section class="piece card card-front" aria-label="Business card front">
  <div class="wordmark"><span>Meridane</span><span>Realty Group LLC</span></div>
</section>

<section class="piece card card-back" aria-label="Business card back">
  <div class="metal-bar" style="height:3px"></div>
  <div class="wordmark"><span>Meridane</span><span>Realty Group LLC</span></div>
  <div class="divider"></div>
  <div class="person">
    <div class="name">R. Daniel Okafor, Esq.</div>
    <div class="title">Managing Broker</div>
    <div class="contact" style="position:static;font-size:4.4px;line-height:5.6px">
      <div class="row"><i class="icon"></i>555.014.2290</div>
      <div class="row"><i class="icon"></i>okafor@meridanerealty.com</div>
      <div class="row"><i class="icon"></i>www.meridanerealty.com</div>
      <div class="addr">1480 W Larkfield Ave.<br>Springdale, IL 60612</div>
    </div>
  </div>
  <div class="navy-bar" style="height:3px"></div>
</section>

</body>
</html>
```